Website design: professional but personally
Needs:
Our visitors are mostly people that look for a IT or technical jobs, but our customers are also visiting our website.
Core values are: personally, professional, ambition, growth, personal development
Terms that we think of are:
Professional, but personal (we ware no trading company, but we do have internation customers)
People
IT (jobs)
Engineering (jobs)

```html
<!DOCTYPE html>
<html lang="nl">
<head>
<meta charset="utf-8">
<title>ProWerk – IT en technisch talent</title>
<link rel="stylesheet" href="https://fonts.googleapis.com/css2?family=Open+Sans:wght@400;600;700;800&family=PT+Sans:wght@400;700&display=swap">
<style>
:root{
  --green:#7dc243;
  --green-dark:#6aae32;
  --ink:#333333;
  --muted:#8a8a8a;
  --dark:#2e2e2e;
  --nav:#3a3a3a;
  --nav-active:#262626;
  --card:#f3f3f3;
  --line:#ececec;
  --white:#ffffff;
}
*{box-sizing:border-box;margin:0;padding:0}
html,body{width:1200px;height:3332px;overflow:hidden}
body{position:relative;background:var(--white);font-family:"Open Sans",Arial,sans-serif;color:var(--ink)}
.abs{position:absolute}
.btn{position:absolute;display:flex;align-items:center;justify-content:center;background:var(--green);color:var(--white);font-weight:700}

/* header */
.site-header{position:absolute;left:0;top:0;width:1200px;height:54px;background:rgba(40,40,40,.85);z-index:3}
.brand{position:absolute;left:98px;top:8px;font-family:"PT Sans",sans-serif;font-weight:700;font-size:32px;letter-spacing:3px;color:var(--white)}
.main-nav{position:absolute;right:96px;top:0;height:54px;display:flex}
.main-nav a{display:flex;align-items:center;padding:0 30px;height:54px;color:var(--white);font-size:14px;font-weight:700;text-decoration:none}
.main-nav a.active{background:var(--nav-active);padding:0 32px}

/* hero */
.hero{position:absolute;left:0;top:0;width:1200px;height:676px}
.hero-photo{position:absolute;inset:0;background:linear-gradient(100deg,#cfcac3 0%,#9c948c 35%,#d9dcdf 60%,#b8bcc0 100%)}
.hero-title{position:absolute;left:598px;top:268px;font-family:"PT Sans",sans-serif;font-weight:700;font-size:62px;letter-spacing:-2px;color:var(--white)}
.hero-text{position:absolute;left:598px;top:344px;width:500px;font-size:15px;line-height:21px;color:var(--white);text-align:justify}
.hero .btn{left:764px;top:420px;width:116px;height:50px;font-size:15px}
.dots{position:absolute;display:flex;gap:8px}
.dots span{width:13px;height:13px;border-radius:50%;background:var(--white)}
.dots span.on{background:var(--green)}

/* services */
.section-title{position:absolute;left:0;width:1200px;text-align:center;color:var(--green);font-family:"PT Sans",sans-serif;font-weight:700}
.service{position:absolute;top:790px;width:312px;height:420px}
.service-head{position:absolute;left:0;top:0;width:312px;height:200px;background:var(--card)}
.service-head svg{position:absolute;left:106px;top:14px}
.service-name{position:absolute;left:0;top:124px;width:312px;text-align:center;font-family:"PT Sans",sans-serif;font-weight:700;font-size:25px;line-height:26px;color:var(--green)}
.service-name b{display:block;color:var(--ink)}
.service p{position:absolute;left:30px;top:212px;width:252px;font-size:13px;line-height:26px;color:var(--muted);text-align:justify}
.service .btn{left:104px;top:380px;width:104px;height:26px;font-size:10px}

/* succes factors band */
.factors{position:absolute;left:0;top:1332px;width:1200px;height:378px;background:linear-gradient(90deg,#2a2d30,#4a4f54 30%,#3b3f43 60%,#2b2e31)}
.factors h2{position:absolute;left:0;top:36px;width:1200px;text-align:center;font-family:"PT Sans",sans-serif;font-weight:700;font-size:34px;color:var(--green)}
.factors h3{position:absolute;left:0;top:122px;width:1200px;text-align:center;font-size:23px;font-weight:700;color:var(--white)}
.factors .rule{position:absolute;left:256px;top:166px;width:688px;height:2px;background:var(--green)}
.factors p{position:absolute;left:256px;top:176px;width:688px;text-align:center;font-size:20px;line-height:32px;color:var(--white)}
.factors svg{position:absolute;top:148px}

/* reasons */
.reasons-title{position:absolute;left:0;top:1756px;width:1200px;text-align:center;font-family:"PT Sans",sans-serif;font-weight:700;font-size:27px;line-height:30px;color:var(--green)}
.reasons-title b{display:block;color:var(--ink)}
.reason{position:absolute;top:1876px;width:252px;height:252px;border-radius:50%;border:2px solid var(--line);text-align:center}
.reason svg{position:absolute;left:96px;top:40px}
.reason p{position:absolute;left:30px;top:118px;width:192px;font-size:13px;line-height:21px;color:#555}
.reason a{position:absolute;left:0;top:176px;width:252px;font-size:11px;font-weight:700;color:var(--green);text-decoration:underline}

/* testimonial */
.testimonial{position:absolute;left:0;top:2170px;width:1200px;height:466px}
.testimonial-photo{position:absolute;inset:0;background:linear-gradient(180deg,#3a3a38 0%,#4a4a46 50%,#2f2f2d 100%)}
.avatar{position:absolute;left:492px;top:66px;width:172px;height:172px;border-radius:50%;border:6px solid var(--green);background:linear-gradient(180deg,#d8d8d8,#9aa2aa)}
.quote{position:absolute;left:246px;top:262px;width:708px;text-align:center;font-size:16px;line-height:26px;color:var(--white)}
.qmark{position:absolute;font-family:"PT Sans",sans-serif;font-size:54px;font-weight:700;color:var(--white);line-height:1}
.person{position:absolute;left:0;top:340px;width:1200px;text-align:center;color:var(--white)}
.person strong{display:block;font-size:16px}
.person span{font-size:13px}

/* staff / map */
.world-map{position:absolute;left:30px;top:2730px;width:650px;height:262px;border-radius:40px;background:radial-gradient(ellipse at center,#c9c9c9 0%,#e4e4e4 60%,#ffffff 100%)}
.staff-title{position:absolute;left:700px;top:2754px;width:380px;text-align:center;font-family:"PT Sans",sans-serif;font-weight:700;font-size:49px;line-height:46px;color:var(--green)}
.staff-sub{position:absolute;left:700px;top:2848px;width:380px;text-align:center;font-size:15px;font-weight:700;line-height:20px;color:var(--green)}
.staff-sub b{display:block;color:var(--ink)}

/* footer */
.site-footer{position:absolute;left:0;top:3048px;width:1200px;height:284px;background:var(--green);color:var(--white)}
.foot-col{position:absolute;top:44px}
.foot-col h4{font-size:15px;font-weight:700;color:#2e3a22;margin-bottom:24px;letter-spacing:.3px}
.foot-col li{list-style:none;font-size:15px;line-height:30px}
.social li{display:flex;align-items:center;gap:16px}
.social i{display:inline-block;width:14px;height:14px;border-radius:50%;background:#2e3a22}
</style>
</head>
<body>

<section class="hero">
  <div class="hero-photo" role="img" aria-label="Foto van een lachende man met een laptop bij een groot raam"></div>
  <h1 class="hero-title">Business Solutions</h1>
  <p class="hero-text">Optimale ondersteuning van uw primaire bedrijfsprocessen? Wij ontzorgen support afdelingen op operationeel gebied: van individueel niveau tot het compleet outsourcen.</p>
  <a class="btn">Read More</a>
  <div class="dots" style="left:556px;top:637px"><span class="on"></span><span></span><span></span><span></span></div>
</section>

<header class="site-header">
  <div class="brand">ProWerk</div>
  <nav class="main-nav">
    <a class="active">HOME</a><a>ONZE DIENSTVERLENING</a><a>VACATURES</a><a>OVER ONS</a>
  </nav>
</header>

<h2 class="section-title" style="top:712px;font-size:34px">ONZE DIENSTEN</h2>

<article class="service" style="left:100px">
  <div class="service-head">
    <svg width="100" height="100" viewBox="0 0 100 100">
      <path d="M4 30 L24 22 L40 52 L22 62 Z" fill="var(--green)"/>
      <path d="M96 30 L76 22 L60 52 L78 62 Z" fill="var(--green)"/>
      <path d="M28 30 L48 26 L58 30 L70 28 L74 52 L56 72 C52 76 46 74 44 70 L30 58 Z" fill="var(--green)"/>
      <path d="M44 36 L58 34 L52 42 Z" fill="#f3f3f3"/>
    </svg>
    <div class="service-name">BUSINESS<b>SOLUTIONS</b></div>
  </div>
  <p>Optimale ondersteuning van uw primaire bedrijfsprocessen? Wij ontzorgen support afdelingen op operationeel gebied: van individueel niveau tot het compleet outsourcen.</p>
  <a class="btn">Read More</a>
</article>

<article class="service" style="left:444px">
  <div class="service-head">
    <svg width="100" height="100" viewBox="0 0 100 100">
      <circle cx="20" cy="22" r="9" fill="#4a4a4a"/><rect x="8" y="34" width="24" height="50" rx="5" fill="#4a4a4a"/>
      <circle cx="80" cy="22" r="9" fill="#4a4a4a"/><rect x="68" y="34" width="24" height="50" rx="5" fill="#4a4a4a"/>
      <circle cx="50" cy="14" r="10" fill="var(--green)"/><rect x="36" y="28" width="28" height="60" rx="6" fill="var(--green)"/>
    </svg>
    <div class="service-name">TALENT<b>SOLUTIONS</b></div>
  </div>
  <p>Talent Solutions richt zich volledig op de sourcing en het ontwikkelen van hoogopgeleid IT en technisch talent. Onze trainees borgen de instroom van kennis binnen ...</p>
  <a class="btn">Read More</a>
</article>

<article class="service" style="left:788px">
  <div class="service-head">
    <svg width="100" height="100" viewBox="0 0 100 100">
      <path d="M50 4 C28 4 16 20 16 36 C16 58 50 90 50 90 C50 90 84 58 84 36 C84 20 72 4 50 4 Z" fill="var(--green)"/>
      <circle cx="50" cy="36" r="22" fill="none" stroke="#f3f3f3" stroke-width="3"/>
      <circle cx="50" cy="28" r="6" fill="#f3f3f3"/><rect x="44" y="36" width="12" height="18" rx="3" fill="#f3f3f3"/>
    </svg>
    <div class="service-name">INTERIM<b>SOLUTIONS</b></div>
  </div>
  <p>Wilt u op korte termijn IT professionals inhuren? Vanuit ons netwerk beschikken wij over de juiste, gekwalificeerde en gedreven medewerker(s) om bij uw bedrijf het verschil ...</p>
  <a class="btn">Read More</a>
</article>

<section class="factors" role="img" aria-label="Foto van een serverruimte met een technicus">
  <h2>ONZE SUCCESFACTOREN</h2>
  <h3>1000+ IT EN TECHNISCHE PROFESSIONALS IN VASTE DIENST</h3>
  <div class="rule"></div>
  <p>Als enige organisatie in Nederland heeft ProWerk ruim 1000 jonge ICT en technische medewerkers voor u klaar staan. ProWerk is een betrouwbare installatiepartner voor de groot zakelijke markt.</p>
  <svg style="left:58px" width="44" height="76" viewBox="0 0 44 76"><path d="M40 4 L6 38 L40 72" fill="none" stroke="var(--green)" stroke-width="5"/></svg>
  <svg style="left:1098px" width="44" height="76" viewBox="0 0 44 76"><path d="M4 4 L38 38 L4 72" fill="none" stroke="var(--green)" stroke-width="5"/></svg>
</section>

<h2 class="reasons-title">SUCCESVOL OMDAT<b>WE HET ANDERS DOEN</b></h2>

<div class="reason" style="left:104px">
  <svg width="60" height="64" viewBox="0 0 60 64"><circle cx="24" cy="24" r="17" fill="none" stroke="var(--green)" stroke-width="3"/><path d="M37 37 L56 58" stroke="var(--green)" stroke-width="4"/></svg>
  <p>IJzersterk in de werving van young professionals</p><a>Know More</a>
</div>
<div class="reason" style="left:358px">
  <svg width="60" height="64" viewBox="0 0 60 64"><path d="M30 4 L37 24 L58 24 L41 37 L47 58 L30 45 L13 58 L19 37 L2 24 L23 24 Z" fill="none" stroke="var(--green)" stroke-width="2.5"/></svg>
  <p>IJzersterk in de werving van young professionals</p><a>Know More</a>
</div>
<div class="reason" style="left:614px">
  <svg width="60" height="64" viewBox="0 0 60 64"><path d="M10 26 A21 21 0 0 1 48 18" fill="none" stroke="var(--green)" stroke-width="2.5"/><path d="M50 38 A21 21 0 0 1 12 46" fill="none" stroke="var(--green)" stroke-width="2.5"/><path d="M40 16 L49 18 L50 8" fill="none" stroke="var(--green)" stroke-width="2.5"/><path d="M20 48 L11 46 L10 56" fill="none" stroke="var(--green)" stroke-width="2.5"/></svg>
  <p>IJzersterk in de werving van young professionals</p><a>Know More</a>
</div>
<div class="reason" style="left:870px">
  <svg width="60" height="64" viewBox="0 0 60 64"><path d="M12 4 L40 4 L50 14 L50 60 L12 60 Z" fill="none" stroke="var(--green)" stroke-width="2.5"/><text x="31" y="44" text-anchor="middle" font-family="Open Sans,sans-serif" font-size="22" fill="var(--green)">€</text></svg>
  <p>IJzersterk in de werving van young professionals</p><a>Know More</a>
</div>

<section class="testimonial">
  <div class="testimonial-photo" role="img" aria-label="Foto van een stadsskyline met wolkenkrabbers"></div>
  <div class="avatar" role="img" aria-label="Portretfoto van Martin in pak"></div>
  <span class="qmark" style="left:202px;top:236px">“</span>
  <p class="quote">Optimale ondersteuning van uw primaire bedrijfsprocessen? Wij ontzorgen support afdelingen op operationeel gebied: van individueel niveau tot het compleet outsourcen.</p>
  <span class="qmark" style="left:944px;top:300px">”</span>
  <div class="person"><strong>Martin</strong><span>Managing Director, Vexa</span></div>
  <div class="dots" style="left:530px;top:424px"><span class="on"></span><span></span><span></span><span></span></div>
</section>

<div class="world-map" role="img" aria-label="Gestippelde wereldkaart met vestigingssteden gemarkeerd"></div>
<h2 class="staff-title">ONZE<br>MEDEWERKERS</h2>
<p class="staff-sub">ZIJN DOOR HEEL NEDERLAND INZETBAAR.<b>WE HEBBEN EEN LANDELIJK DEKKEND PERSONEELSBESTAND.</b></p>

<footer class="site-footer">
  <div class="foot-col" style="left:108px"><h4>ADRESGEGEVENS</h4><ul><li>ProWerk B.V.</li><li>Keizersweg 120B</li><li>1017 AB Amsterdam</li><li>0880 123 456</li><li>Privacy Policy</li></ul></div>
  <div class="foot-col" style="left:362px"><h4>VOOR OPDRACHTGEVERS</h4><ul><li>Klanten over ProWerk</li><li>Login urenregistratiesysteem</li><li>Nieuws</li></ul></div>
  <div class="foot-col" style="left:650px"><h4>VOOR WERKZOEKENDEN</h4><ul><li>IT Traineeship</li><li>Technisch Traineeship</li><li>Werken en leren in de ICT</li><li>Sollicitatietips</li></ul></div>
  <div class="foot-col social" style="left:936px"><h4>CONNECT</h4><ul><li><i></i>Kwetter</li><li><i></i>Vriendnet</li><li><i></i>Netwerkhub</li><li><i></i>Kijkkanaal</li></ul></div>
</footer>

</body>
</html>
```